Mortgage Broking boutique Business

I’m wanting a revamped look to my existing business card design. I do like the black and silver but happy to have other colours introduced based on your creation. I’ve attached a copy of my current card so you can have a starting point updated details noted brloe. I deal with high net worth individuals so need my card to be sophisticated, classy that gives off a classy vibe

Target Market(s)

High net worth, wealthy

Industry/Entity Type

Mortgage Brokerage

Contact Information for Business Card

Job title: Finance Executive
Phone: +61 7 3862 1197
Mobile: 0431 275 506
Email: marcus@quillbrookcapital.com.au
Web: www.quillbrookcapital.com.au
Address: level 22 Tamberlin House, 48 Mercer Rd Brisbane QLD 4000

Font styles to use
Other font styles liked:
• Helvetica

Colors

Designer to choose colors to be used in the design.

Requirements
Must have
• Use my existing card design as a starting point

```html
<!DOCTYPE html>
<html lang="en">
<head>
<meta charset="utf-8">
<title>Quillbrook Capital – Business Card</title>
<link href="https://fonts.googleapis.com/css2?family=Jost:wght@500&family=Open+Sans:wght@400&family=PT+Sans+Narrow:wght@400&display=swap" rel="stylesheet">
<style>
  :root {
    --paper: #ffffff;
    --ink: #141516;
    --silver-dark: #b9babd;
    --silver-mid: #cfd0d3;
    --silver-light: #eef0f1;
    --streak: rgba(255,255,255,0.12);
    --groove: rgba(120,122,126,0.05);
    --on-ink: #f2f2f2;
  }
  * { margin: 0; padding: 0; box-sizing: border-box; }
  html, body { width: 1200px; height: 537px; overflow: hidden; background: var(--paper); }
  .canvas { position: relative; width: 1200px; height: 537px; }

  .card {
    position: absolute;
    top: 113px;
    width: 506px;
    height: 295px;
    overflow: hidden;
    background:
      repeating-linear-gradient(180deg, var(--groove) 0 1px, transparent 1px 3px, var(--streak) 3px 4px, transparent 4px 6px),
      linear-gradient(90deg,
        var(--silver-dark) 0%, var(--silver-mid) 18%, var(--silver-mid) 40%,
        var(--silver-light) 52%, var(--silver-light) 56%, var(--silver-mid) 66%,
        var(--silver-mid) 86%, var(--silver-dark) 100%);
  }
  .card--front { left: 61px; }
  .card--back { left: 605px; }

  .brand {
    position: absolute;
    inset: 0;
    display: flex;
    flex-direction: column;
    align-items: center;
    justify-content: center;
    font-family: "Jost", sans-serif;
    font-weight: 500;
    color: var(--ink);
    text-transform: uppercase;
    padding-top: 6px;
  }
  .brand__name { font-size: 38px; letter-spacing: 5px; line-height: 1; }
  .brand__sub { font-size: 26px; letter-spacing: 6px; line-height: 1; margin-top: 16px; }

  .title-band {
    position: absolute;
    left: 0; top: 104px;
    width: 249px; height: 88px;
    background: var(--ink);
    display: flex; align-items: center; justify-content: center;
    padding-left: 10px;
  }
  .title-band__text {
    font-family: "PT Sans Narrow", sans-serif;
    font-size: 30px;
    color: var(--on-ink);
  }

  .contact { position: absolute; left: 282px; display: flex; align-items: center; }
  .contact__icon {
    width: 34px; height: 34px; border-radius: 6px;
    background: var(--ink);
    display: flex; align-items: center; justify-content: center;
    flex-shrink: 0;
  }
  .contact__icon svg { width: 20px; height: 20px; fill: var(--on-ink); stroke: var(--on-ink); }
  .contact__text {
    margin-left: 10px;
    font-family: "Open Sans", sans-serif;
    font-size: 10px;
    letter-spacing: -0.1px;
    color: var(--ink);
    line-height: 1.3;
    white-space: nowrap;
  }
  .contact__text--address { text-align: center; margin-top: -6px; }
  .contact__text--phone { font-size: 11px; letter-spacing: 0.4px; margin-top: -6px; }
  .contact--address { top: 54px; }
  .contact--email { top: 119px; }
  .contact--phone { top: 179px; }
  .contact--web { top: 238px; }
</style>
</head>
<body>
<div class="canvas">

  <section class="card card--front">
    <div class="brand">
      <span class="brand__name">Quillbrook</span>
      <span class="brand__sub">Capital</span>
    </div>
  </section>

  <section class="card card--back">
    <div class="title-band"><span class="title-band__text">Finance Executive</span></div>

    <div class="contact contact--address">
      <span class="contact__icon">
        <svg viewBox="0 0 20 20" stroke-width="0"><path d="M10 2a5.5 5.5 0 0 0-5.5 5.5C4.5 12 10 18 10 18s5.5-6 5.5-10.5A5.5 5.5 0 0 0 10 2zm0 7.6a2.1 2.1 0 1 1 0-4.2 2.1 2.1 0 0 1 0 4.2z"/></svg>
      </span>
      <span class="contact__text contact__text--address">level 22 Tamberlin House, 48<br>Mercer Rd Brisbane QLD 4000</span>
    </div>

    <div class="contact contact--email">
      <span class="contact__icon">
        <svg viewBox="0 0 20 20"><rect x="2.5" y="5" width="15" height="10" fill="none" stroke-width="1.4"/><path d="M2.5 5l7.5 6 7.5-6M2.5 15l5.5-5M17.5 15l-5.5-5" fill="none" stroke-width="1.4"/></svg>
      </span>
      <span class="contact__text">marcus@quillbrookcapital.com.au</span>
    </div>

    <div class="contact contact--phone">
      <span class="contact__icon">
        <svg viewBox="0 0 20 20" stroke-width="0"><path d="M6.2 3.2l2 3.2c.3.5.2 1-.2 1.4l-1 1c.8 1.7 2.2 3.1 3.9 3.9l1-1c.4-.4.9-.5 1.4-.2l3.2 2c.5.3.6.9.3 1.4l-1.1 1.6c-.4.6-1.2.9-1.9.7C8.8 16 4 11.2 2.8 6.2c-.2-.7.1-1.5.7-1.9L5 3c.4-.3 1-.2 1.2.2z"/></svg>
      </span>
      <span class="contact__text contact__text--phone">+61 7 3862 1197</span>
    </div>

    <div class="contact contact--web">
      <span class="contact__icon">
        <svg viewBox="0 0 20 20" fill="none" stroke-width="1.2"><circle cx="10" cy="10" r="7.5" fill="none"/><ellipse cx="10" cy="10" rx="3.3" ry="7.5" fill="none"/><path d="M2.5 10h15M3.6 6.2h12.8M3.6 13.8h12.8M10 2.5v15" fill="none"/></svg>
      </span>
      <span class="contact__text">www.quillbrookcapital.com.au</span>
    </div>
  </section>

</div>
</body>
</html>
```